"The Summit Hour Audio Series" needs 3 banner ad designs

I am seeking the design and creation of 3 differently-designed ”banner ads.” I want them to look as though there is a relation between designs but I don't want them to look the same.
While compatibility is desired, that desire should not be interpreted as sameness.

I need a series of banner ads to be a supplement and a complement to
"The Summit Hour"'s main banner ad page and accompanying site.
http://www.quorvale.org/

I am looking for high quality, creative capturing of banner ads that focus on three topic areas, namely, my:

1. Leadership Coaching Program –
“Stride Builder Mentoring Track™”

2. Training program – “The Craft of a Steady Captain”

and

3. Speaker Interest & Availability banner ad.

It is desired that each banner, and the banners collectively, complement and fit in with the look and feel of the existing, principal banner and the show’s vision and mission. (in the attachment, I have included a copy of this banner for your information).

The final design should commit experience, competence, depth and reliability.

To provide a bit of context for this request, I have included the show's vision and mission statement as well as a brief description of my perspective on each banner ad.

I will of course, provide the winner all of the information, documents, graphic depictions, etc that I have available (during the handover stage) that will enable them to create quality products.

In addition, each banner ad should be delivered as JPEG files in dimensions 728 pixel wide and 90 pixels high each. The following fonts: Trajan Pro Regular or Thomas Condensed Regular are the desired fonts.

The task summary: Design 3 banner ads as described below:

1. Leadership Coaching Program – Stride Builder Mentoring Track™
My coaching program has a formal structure that has an existing graphic capturing of leadership coaching that that would/should be incorporated in the ad.

2. Training program – The Craft of a Steady Captain
The skills training program description I have included as noted below; it is a program that can also be licensed for use by customers who would wish to use it in their organization. In addition to the creative thinking of graphics artists, it would probably be useful to view the home page graphic at www.tovrik4.com. This image might be useful in enhancing the banner ad graphic.

3. Speaking Interest – Availability
Have been and desire using this banner to communicate my interest in generating value and availability as a speaker.

-Vision-
“The Summit Hour”
Making an Impact through Effective Leadership
*is a powerfully engaging platform for great conversations about leadership and leadership learning.

-Mission-
Build a community of listeners who are informed and enthusiastically engaged with the host and the show’s goal of improving the quality of leadership wherever listeners are living and leading.

File: "1785 Postcard V2" - *this information is for use in designing the
Leadership Coaching Banner Ad* = *Stride Builder Mentoring Track*

File: "Cover Shot of Skills Book" - *this information is
for use in designing the Book Ad – The Craft of a Steady Captain:
Growing a Guide Whom Peers Gladly Trust*

File: (word doc) The Craft of a Steady Captain Training Workshop – Skills &
Concepts Summary *this information is for the design of the banner ad for
the Skills Training Course. It includes quotes that could be excerpted to
include in the banner ad*

File name: "Cover - Craft of a Steady Captain"
-> Picture of book for Craft of a Steady Captain Training Program – *this is additional information for the use in designing the Training program banner ad

You can find the other attachments useful. Please have a look.
I welcome all your creative and original designs. Remember, these are 3 different-looking banner ads - though related in some way.

Project Deadline Extended Reason: The current designs have not included enough variety and creativity. While I am desirous of compatibility of the ad renditions with the central image, I am not interpreting compatibility with sameness of looking to see the same image in each banner ad. I rather think the image differentiation promotes both interest and distinction between the products of book, leadership coaching, speaking, etc. Same image embedded in each banner ad doesn't provide the variety that I think both distinguishes and draws interest. In this regard, most of the current examples include the same pictorial images across designs and the use of just words vs. images from among those provided, As an example a picture of my book on the book banner ad seems more impactful than merely using the words book on the ad for the book; and the picture of a speaker vs. Speaker Availability.I hope this feedback is helpful . Regards,Leopold Added Saturday, June 3, 2017

Target Market(s)

Online Radio Listeners Can Visit WavelineHub.com for examples - Will be broadcast on the Commerce Channel

Industry/Entity Type

Business Consultant

Colors

Designer to choose colors to be used in the design.

Requirements
Should not have
• Anything that doesn't speak to the characteristics noted at the end of the summary provided in the description above

```html
<!DOCTYPE html>
<html lang="en">
<head>
<meta charset="utf-8">
<title>Speaker Interest &amp; Availability Banner</title>
<link rel="stylesheet" href="https://fonts.googleapis.com/css2?family=Cinzel:wght@400&display=swap">
<style>
  :root {
    --steel-deep: #6f8fae;
    --steel-mid: #9fb6cc;
    --steel-light: #d3dfea;
    --frame-white: #f4f7fa;
    --ink-navy: #1c2946;
    --rule: rgba(28, 41, 70, 0.35);
    --photo-warm-a: #8a7a72;
    --photo-warm-b: #c9b7a6;
    --photo-cool-a: #5d6f80;
    --photo-cool-b: #b8c4cf;
  }
  html, body {
    margin: 0;
    padding: 0;
    width: 1200px;
    height: 148px;
    overflow: hidden;
    background: #ffffff;
  }
  .banner {
    position: relative;
    width: 1200px;
    height: 148px;
    overflow: hidden;
    background: linear-gradient(180deg, var(--steel-light) 0%, var(--steel-mid) 55%, var(--steel-deep) 100%);
    font-family: "Cinzel", "Trajan Pro", serif;
  }
  .banner__glow {
    position: absolute;
    left: 360px;
    top: -40px;
    width: 560px;
    height: 230px;
    background: radial-gradient(ellipse at center, rgba(255,255,255,0.55) 0%, rgba(255,255,255,0) 70%);
  }
  .banner__art {
    position: absolute;
    inset: 0;
    width: 1200px;
    height: 148px;
  }
  .banner__frame {
    position: absolute;
    inset: 4px;
    border: 2px solid var(--frame-white);
    pointer-events: none;
  }
  .headline {
    position: absolute;
    left: 430px;
    top: 22px;
    width: 420px;
    margin: 0;
    color: var(--ink-navy);
    font-weight: 400;
    text-align: center;
  }
  .headline__line {
    display: block;
    line-height: 1;
  }
  .headline__line--top {
    font-size: 40px;
    letter-spacing: 0.5px;
  }
  .headline__rule {
    display: block;
    width: 400px;
    height: 1px;
    margin: 9px auto 8px;
    background: var(--rule);
  }
  .headline__line--bottom {
    font-size: 50px;
    letter-spacing: 0.5px;
  }
</style>
</head>
<body>
  <div class="banner">
    <div class="banner__glow"></div>
    <svg class="banner__art" viewBox="0 0 1200 148" xmlns="http://www.w3.org/2000/svg">
      <defs>
        <linearGradient id="audienceTone" x1="0" y1="0" x2="1" y2="1">
          <stop offset="0" stop-color="var(--photo-warm-b)"/>
          <stop offset="0.5" stop-color="var(--photo-warm-a)"/>
          <stop offset="1" stop-color="#6e5f5a"/>
        </linearGradient>
        <linearGradient id="audienceFade" x1="0" y1="0" x2="1" y2="0">
          <stop offset="0.7" stop-color="#ffffff" stop-opacity="1"/>
          <stop offset="1" stop-color="#ffffff" stop-opacity="0"/>
        </linearGradient>
        <mask id="audienceMask">
          <rect x="0" y="0" width="420" height="148" fill="url(#audienceFade)"/>
        </mask>
        <linearGradient id="speakerTone" x1="0" y1="0" x2="1" y2="1">
          <stop offset="0" stop-color="var(--photo-cool-b)"/>
          <stop offset="0.55" stop-color="var(--photo-cool-a)"/>
          <stop offset="1" stop-color="#c9c2a8"/>
        </linearGradient>
      </defs>
      <g role="img" aria-label="Photo of a diverse group seated around a conference table in a workshop">
        <polygon points="0,0 410,0 360,148 0,148" fill="url(#audienceTone)" mask="url(#audienceMask)"/>
      </g>
      <g role="img" aria-label="Photo of the speaker, an older man in glasses, listening thoughtfully">
        <polygon points="975,0 1200,0 1200,148 950,148" fill="url(#speakerTone)"/>
        <line x1="975" y1="0" x2="950" y2="148" stroke="var(--frame-white)" stroke-width="3"/>
      </g>
    </svg>
    <div class="banner__frame"></div>
    <h1 class="headline">
      <span class="headline__line headline__line--top">Speaker Interest</span>
      <span class="headline__rule"></span>
      <span class="headline__line headline__line--bottom">&amp; Availability</span>
    </h1>
  </div>
</body>
</html>
```